IT business looking for Standout Letterhead Design

We need a letterhead design for a company based in Harrow Point, CA called Corvane Systems, Inc. We specialize in IT engineering, installation and technical support pertaining to the department of defense.

We would like to see a design that incorporates the black and gold that matches our company logo.

More information on the company can be found at www.corvane-sys.example

```html
<!DOCTYPE html>
<html lang="en">
<head>
<meta charset="utf-8">
<title>Corvane Systems, Inc. — Letterhead</title>
<link rel="stylesheet" href="https://fonts.googleapis.com/css2?family=Source+Sans+3:wght@400;600&display=swap">
<style>
  :root {
    --paper: #ffffff;
    --ink: #1d1b1c;
    --gold: #c8952a;
    --gold-deep: #a8701f;
    --gold-light: #f2d33a;
    --black-band: #231f20;
    --watermark: #e6e6e6;
  }
  html, body {
    margin: 0;
    padding: 0;
    overflow: hidden;
    background: var(--paper);
  }
  .letterhead {
    position: relative;
    width: 900px;
    height: 1200px;
    overflow: hidden;
    background: var(--paper);
    font-family: "Source Sans 3", Arial, sans-serif;
    color: var(--ink);
  }
  .brand {
    position: absolute;
    left: 40px;
    top: 122px;
    display: flex;
    align-items: center;
    gap: 12px;
  }
  .brand-mark {
    width: 18px;
    height: 18px;
    background: var(--gold);
  }
  .brand-name {
    font-size: 26px;
    font-weight: 600;
    color: var(--ink);
    letter-spacing: 0.5px;
  }
  .contact {
    position: absolute;
    left: 697px;
    top: 58px;
    margin: 0;
    font-style: normal;
    font-size: 14px;
    line-height: 18.3px;
    color: var(--ink);
  }
  .watermark {
    position: absolute;
    left: 0;
    width: 900px;
    top: 640px;
    text-align: center;
    font-weight: 400;
    color: var(--watermark);
    line-height: 1;
  }
  .watermark-name { font-size: 140px; letter-spacing: 6px; }
  .watermark-sub { font-size: 40px; letter-spacing: 4px; margin-top: 20px; }
  .footer-rule {
    position: absolute;
    left: 0;
    bottom: 46px;
    width: 900px;
    height: 4px;
    background: var(--black-band);
  }
  .footer-band {
    position: absolute;
    left: 0;
    bottom: 0;
    width: 900px;
    height: 40px;
    background: linear-gradient(90deg, var(--gold-light) 0%, var(--gold) 45%, var(--gold-deep) 100%);
  }
</style>
</head>
<body>
<main class="letterhead">
  <header>
    <div class="brand">
      <span class="brand-mark"></span>
      <span class="brand-name">Corvane Systems, Inc.</span>
    </div>
    <address class="contact">
      Corvane Systems, Inc.<br>
      Harrow Point, CA<br>
      555-204-0148<br>
      555-204-0172<br>
      info@corvane-sys.example<br>
      www.corvane-sys.example
    </address>
  </header>

  <div class="watermark" aria-hidden="true">
    <div class="watermark-name">CORVANE</div>
    <div class="watermark-sub">SYSTEMS, INC.</div>
  </div>

  <footer>
    <div class="footer-rule"></div>
    <div class="footer-band"></div>
  </footer>
</main>
</body>
</html>
```